PowerPoint template for my training workshop business

I would like to have a PowerPoint template created using my logo and palette materials created by Brivantelox. I train and facilitate workshops using PowerPoint in both corporate and public settings.

I have attached the original design elements to this request.

```html
<!DOCTYPE html>
<html lang="en">
<head>
<meta charset="utf-8">
<title>Lumera Vance Coaching – Workshop Template</title>
<link href="https://fonts.googleapis.com/css2?family=Montserrat:wght@400;600;800&family=Open+Sans:ital,wght@1,700&display=swap" rel="stylesheet">
<style>
  :root{
    --board:#525a5b;
    --paper:#f7f9fb;
    --teal:#0c3b45;
    --grey:#9c9d9c;
    --grey-soft:#d9d9d9;
    --bar-mid:#a6b0ba;
    --bar-light:#c6d5e2;
    --bar-pale:#d6e4f0;
    --accent:#f0a021;
    --white:#ffffff;
  }
  *{margin:0;padding:0;box-sizing:border-box}
  html,body{width:1200px;height:734px;overflow:hidden;background:var(--board)}
  body{position:relative;font-family:"Montserrat",sans-serif}
  .slide{position:absolute;width:520px;height:293px;background:var(--paper);overflow:hidden;box-shadow:2px 3px 6px rgba(0,0,0,.35)}
  .slide svg.shapes{position:absolute;left:0;top:0;width:520px;height:293px}
  .s1{left:49px;top:39px}
  .s2{left:634px;top:39px}
  .s3{left:49px;top:397px}
  .s4{left:634px;top:397px}

  .brand{position:absolute;display:flex;align-items:center;gap:5px;color:var(--accent);font-family:"Montserrat",sans-serif;font-weight:600;line-height:1.05}
  .brand .dot{border-radius:50%;background:var(--accent);flex:none}
  .brand .name{letter-spacing:.02em}
  .brand .name small{display:block;font-size:.62em;letter-spacing:.25em;text-align:center}
  .brand-lg{left:20px;top:13px;font-size:11px}
  .brand-lg .dot{width:30px;height:30px}
  .brand-sm{right:15px;top:10px;font-size:7px}
  .brand-sm .dot{width:19px;height:19px}

  .title{position:absolute;font-family:"Montserrat",sans-serif;font-weight:800;line-height:1.05;letter-spacing:.01em;color:var(--teal)}
  .body{position:absolute;font-size:5.8px;line-height:8.5px;color:#2c3a3f;font-family:"Montserrat",sans-serif}

  /* slide 1 */
  .s1 .title-box{position:absolute;left:260px;top:95px;width:204px;height:64px;background:rgba(255,255,255,.8)}
  .s1 .title{left:276px;top:102px;font-size:25px}
  .s1 .rule{position:absolute;left:481px;top:226px;width:16px;height:2px;background:var(--white)}
  .s1 .body{right:23px;top:233px;text-align:right;color:var(--white)}

  /* slide 2 */
  .s2 .title{left:284px;top:86px;font-size:24px}
  .s2 .body{left:313px;top:174px;width:160px}

  /* slide 3 */
  .s3 .title{left:61px;top:49px;font-size:25px;color:var(--white)}
  .s3 .points{position:absolute;left:65px;top:121px;list-style:none}
  .s3 .points li{position:relative;padding-left:12px;font-size:5.8px;line-height:8.4px;color:var(--white);width:140px;margin-bottom:17px}
  .s3 .points li::before{content:"";position:absolute;left:0;top:5px;border-left:6px solid var(--white);border-top:3.5px solid transparent;border-bottom:3.5px solid transparent}

  /* slide 4 */
  .s4 .title{left:0;width:536px;text-align:center;top:63px;font-size:25px}
  .s4 .stat{position:absolute;top:196px;width:100px;text-align:center}
  .s4 .stat h3{font-family:"Open Sans",sans-serif;font-style:italic;font-weight:700;font-size:9px;color:#1f2c30;letter-spacing:.04em}
  .s4 .stat p{margin-top:5px;font-size:4.8px;line-height:6.4px;color:#3b4649}
</style>
</head>
<body>

<!-- Cover slide -->
<section class="slide s1">
  <svg class="shapes" viewBox="0 0 520 293" aria-hidden="true">
    <polygon points="323,0 520,0 520,293 129,293" fill="var(--teal)"/>
  </svg>
  <svg class="shapes" viewBox="0 0 520 293">
    <defs>
      <linearGradient id="sky1" x1="0" y1="0" x2="1" y2="1">
        <stop offset="0" stop-color="#a7b3bd"/>
        <stop offset=".55" stop-color="#7f95a6"/>
        <stop offset="1" stop-color="#b9c4cc"/>
      </linearGradient>
    </defs>
    <rect x="0" y="57" width="403" height="206" fill="url(#sky1)" role="img" aria-label="Photo of glass office towers against a cloudy sky"/>
  </svg>
  <div class="brand brand-lg"><span class="dot"></span><span class="name">LUMERA VANCE<small>COACHING</small></span></div>
  <div class="title-box"></div>
  <h1 class="title">WORKSHOP<br>TITLE</h1>
  <div class="rule"></div>
  <p class="body">Lorem ipsum dolor sit<br>amet, consectetuer<br>adipiscing elit, sed<br>diam nonummy nibh</p>
</section>

<!-- Section slide -->
<section class="slide s2">
  <svg class="shapes" viewBox="0 0 520 293">
    <defs>
      <linearGradient id="sky2" x1="0" y1="1" x2="1" y2="0">
        <stop offset="0" stop-color="#6e9cc0"/>
        <stop offset=".6" stop-color="#a9c3d6"/>
        <stop offset="1" stop-color="#dfe5e8"/>
      </linearGradient>
    </defs>
    <polygon points="0,0 382,0 192,293 0,293" fill="var(--teal)"/>
    <polygon points="28,23 367,23 208,269 28,269" fill="url(#sky2)" role="img" aria-label="Photo looking up at a curved glass skyscraper"/>
  </svg>
  <div class="brand brand-sm"><span class="dot"></span><span class="name">LUMERA VANCE<small>COACHING</small></span></div>
  <h2 class="title">LOREM DOLOR<br>IPSUM SIT</h2>
  <p class="body">Lorem ipsum dolor sit amet, consectetuer adipiscing elit, sed diam nonummy nibh euismod tincidunt ut laoreet dolore magna aliquam erat volutpat. Ut wisi enim ad minim veniam, quis nostrud exerci tation ullamcorper suscipit lobortis nisl ut aliquip ex ea commodo consequat. Duis autem vel eum iriure dolor in hendrerit in vulputate velit esse</p>
</section>

<!-- Bullet slide -->
<section class="slide s3">
  <svg class="shapes" viewBox="0 0 520 293">
    <defs>
      <linearGradient id="sky3" x1="0" y1="0" x2="1" y2="1">
        <stop offset="0" stop-color="#dfe4e8"/>
        <stop offset=".5" stop-color="#b7c7d4"/>
        <stop offset="1" stop-color="#8e9ea9"/>
      </linearGradient>
    </defs>
    <polygon points="263,62 520,62 520,293 129,293" fill="var(--grey)"/>
    <rect x="214" y="62" width="283" height="205" fill="url(#sky3)" role="img" aria-label="Photo of a white building facade under a pale sky"/>
    <polygon points="28,25 188,25 346,269 28,269" fill="var(--teal)"/>
  </svg>
  <div class="brand brand-sm"><span class="dot"></span><span class="name">LUMERA VANCE<small>COACHING</small></span></div>
  <h2 class="title">LOREM<br>IPSUM SIT</h2>
  <ul class="points">
    <li>Lorem ipsum dolor sit amet, consectetuer adipiscing elit, sed diam nonummy nibh euismod tincidunt ut laoreet dolore magna</li>
    <li>Lorem ipsum dolor sit amet, consectetuer adipiscing elit, sed diam nonummy nibh euismod tincidunt ut laoreet dolore magna</li>
    <li>Lorem ipsum dolor sit amet, consectetuer adipiscing elit, sed diam nonummy nibh euismod tincidunt ut laoreet dolore magna</li>
  </ul>
</section>

<!-- Chart slide -->
<section class="slide s4">
  <svg class="shapes" viewBox="0 0 520 293">
    <polygon points="65,0 131,0 0,179 0,88" fill="var(--teal)"/>
    <polygon points="520,105 520,293 377,293" fill="var(--grey-soft)"/>
    <g class="chart">
      <rect x="55" y="133" width="10" height="46" fill="var(--teal)"/>
      <rect x="66" y="123" width="10" height="56" fill="var(--bar-mid)"/>
      <rect x="77" y="133" width="10" height="46" fill="var(--bar-light)"/>
      <rect x="88" y="144" width="10" height="35" fill="var(--bar-pale)"/>

      <rect x="174" y="138" width="10" height="41" fill="var(--bar-pale)"/>
      <rect x="185" y="138" width="10" height="41" fill="var(--bar-light)"/>
      <rect x="196" y="128" width="10" height="51" fill="var(--bar-mid)"/>
      <rect x="207" y="125" width="10" height="54" fill="var(--teal)"/>

      <rect x="293" y="128" width="10" height="51" fill="var(--teal)"/>
      <rect x="304" y="131" width="10" height="48" fill="var(--bar-mid)"/>
      <rect x="315" y="142" width="10" height="37" fill="var(--bar-light)"/>
      <rect x="326" y="138" width="10" height="41" fill="var(--bar-pale)"/>

      <rect x="406" y="131" width="10" height="48" fill="var(--bar-pale)"/>
      <rect x="417" y="136" width="10" height="43" fill="var(--bar-light)"/>
      <rect x="428" y="129" width="10" height="50" fill="var(--bar-mid)"/>
      <rect x="439" y="119" width="10" height="60" fill="var(--teal)"/>
    </g>
  </svg>
  <div class="brand brand-sm"><span class="dot"></span><span class="name">LUMERA VANCE<small>COACHING</small></span></div>
  <h2 class="title">LOREM IPSUM SIT</h2>
  <div class="stat" style="left:27px"><h3>Lorem ipsum</h3><p>Lorem ipsum dolor sit amet,<br>consectetuer adipiscing<br>elit, sed diam nonummy nibh<br>euismod tincidunt ut<br>laoreet dolore magna</p></div>
  <div class="stat" style="left:146px"><h3>Lorem ipsum</h3><p>Lorem ipsum dolor sit amet,<br>consectetuer adipiscing<br>elit, sed diam nonummy nibh<br>euismod tincidunt ut<br>laoreet dolore magna</p></div>
  <div class="stat" style="left:265px"><h3>Lorem ipsum</h3><p>Lorem ipsum dolor sit amet,<br>consectetuer adipiscing<br>elit, sed diam nonummy nibh<br>euismod tincidunt ut<br>laoreet dolore magna</p></div>
  <div class="stat" style="left:378px"><h3>Lorem ipsum</h3><p>Lorem ipsum dolor sit amet,<br>consectetuer adipiscing<br>elit, sed diam nonummy nibh<br>euismod tincidunt ut<br>laoreet dolore magna</p></div>
</section>

</body>
</html>
```